Medical centre needs a business card

We are a medcial centre in Australia, needing a new business card. Our demographic is low working class families. We are going to be renovating our premises to modernise the look and also had a new logo done a few months ago representing quality and community, and now need to update our cards. It needs to be doubled sided, with logo and contact details on the front, and appointment details on the back. . Needs to be modern and simple, easy to read. <br/><br/>Name: Kindle Grove Medical Centre <br/>Address: 512 Tolvar Rd (Cnr Tolvar Rd & Quenby Park Rd),<br/>Dunmarra Court Shopping Centre, Corrin Vale, SA 5921<br/>Ph: 08 8194 3627<br/>Tag line: Where your care comes first<br/>Website: www.kindlegrovemedicalcentre-example.com.au<br/>Online bookings also available<br/><br/>(On the back, to have 3 lines of appointments that can be written in.<br/>Day, date, time)<br/><br/>Your next appointment is on<br/>Can try “M T W Th F Sa Su _________________ at ____________ am/pm” or other combinations <br/>Please advise as soon as possible if unable to attend<br/>Cancellation fees apply if less than 2 hrs notice<br/>Online appointments available (please highlight this option by either by position, colour or font)

Target Market(s)

Lower social economic working class, young families to seniors

Industry/Entity Type

Medical Centre

Contact Information for Business Card

Kindle Grove Medical Centre
512 Tolvar Rd (Cnr Tolvar Rd & Quenby Park Drive)
Dunmarra Court Shopping Centre
Corrin Vale SA 5921
Ph: 08 8194 3627
www.kindlegrovemedicalcentre-example.com.au
Tagline line: where your care comes first
Back side is for appointments
Your next appointment is with Dr ______________
Day/date/time (Please give 3 lines of appointments)
Please advise as soon as possible if unable to attend
Cancellation fees apply if less than 2 hours notice
Online appointments available
Book online easily and conveniently (please highlight online appointments)

Font styles to use
Serif
Sans Serif

Colors

Designer to choose colors to be used in the design.

Requirements
Must have
• Modern and simple
• Easy to ready
• Induces a wellbeing feeling
• Incorporate our logo colours and feel from logo
• Induces feeling of stability and security
Nice to have
• Attract attention
• Pleasant to look at
• Feeling of innovation
Should not have
• Loud clashing colours
• Overly luxurious feeling
• Overly artistic

```html
<!DOCTYPE html>
<html lang="en">
<head>
<meta charset="utf-8">
<title>Kindle Grove Medical Centre – Business Card</title>
<link rel="stylesheet" href="https://fonts.googleapis.com/css2?family=Mulish:wght@300;400;800&display=swap">
<style>
  :root {
    --backdrop: #1d1d1f;
    --card: #f4f4f6;
    --blue-deep: #0f6fbf;
    --blue-bright: #22a4de;
    --green: #9fcb3d;
    --green-text: #a3c84a;
    --ink: #3c3c44;
    --white: #ffffff;
    --faint-name: #b9c9e4;
  }
  * { box-sizing: border-box; margin: 0; padding: 0; }
  html, body { width: 1131px; height: 1200px; overflow: hidden; }
  body {
    background: var(--backdrop);
    font-family: "Mulish", sans-serif;
    position: relative;
  }
  .card {
    position: absolute;
    width: 781px;
    height: 447px;
    background: var(--card);
    overflow: hidden;
  }
  .card--front { left: 153px; top: 107px; }
  .card--back { left: 152px; top: 598px; }

  /* Front */
  .brand {
    position: absolute;
    left: 0; right: 0; top: 118px;
    text-align: center;
  }
  .brand__mark {
    display: block;
    width: 26px; height: 26px;
    margin: 0 auto 16px;
    background: var(--blue-deep);
    border-radius: 50%;
  }
  .brand__name {
    font-weight: 800;
    font-size: 34px;
    letter-spacing: 0.5px;
    color: var(--blue-deep);
    text-transform: uppercase;
    white-space: nowrap;
  }
  .contact-panel {
    position: absolute;
    left: 0; top: 240px;
    width: 781px; height: 207px;
  }
  .contact-panel svg { position: absolute; left: 0; top: 0; }
  .tagline {
    position: absolute;
    left: 0; right: 0; top: 12px;
    text-align: center;
    color: var(--white);
    font-weight: 300;
    font-size: 24px;
  }
  .address {
    position: absolute;
    left: 34px; top: 92px;
    color: var(--white);
    font-size: 17px;
    line-height: 22.5px;
    font-weight: 400;
    font-style: normal;
  }
  .links {
    position: absolute;
    left: 400px; top: 122px;
    list-style: none;
    color: var(--white);
    font-size: 16px;
    white-space: nowrap;
  }
  .links li {
    display: flex; align-items: center;
    height: 24px; margin-bottom: 8px;
  }
  .links__icon {
    flex: none;
    width: 24px; height: 24px;
    background: var(--green);
    margin-right: 14px;
    display: flex; align-items: center; justify-content: center;
  }

  /* Back */
  .appointment__title {
    position: absolute;
    left: 64px; top: 102px;
    font-weight: 300;
    font-size: 28px;
    color: var(--green-text);
  }
  .appointment__fields { position: absolute; left: 64px; top: 202px; }
  .field {
    display: flex; align-items: flex-end;
    height: 26px; margin-bottom: 38px;
    font-size: 17px; color: var(--ink);
  }
  .field__label { width: 51px; }
  .field__line {
    width: 355px; height: 1px;
    border-bottom: 2px dotted var(--ink);
    margin-bottom: 5px;
  }
  .booking-bubble { position: absolute; left: 515px; top: 8px; }
  .booking-bubble__text {
    position: absolute;
    left: 533px; top: 88px;
    width: 220px;
    text-align: center;
    color: var(--green);
    transform: rotate(-12deg);
  }
  .booking-bubble__lead { font-size: 28px; font-weight: 400; display: block; }
  .booking-bubble__sub { font-size: 13px; font-weight: 400; display: block; margin-top: 2px; }
  .brand--faint {
    position: absolute;
    left: 478px; right: auto; top: 318px;
    width: 300px;
    text-align: center;
  }
  .brand--faint .brand__name {
    color: var(--faint-name);
    font-size: 15px;
    letter-spacing: 0;
  }
  .notice-strip {
    position: absolute;
    left: 0; top: 377px;
    width: 781px; height: 34px;
    background: linear-gradient(90deg, var(--blue-deep), var(--blue-bright));
    color: var(--white);
    font-size: 16px;
    line-height: 34px;
    text-align: center;
    white-space: nowrap;
  }
</style>
</head>
<body>

<section class="card card--front" aria-label="Business card front">
  <div class="brand">
    <span class="brand__mark"></span>
    <p class="brand__name">Kindle Grove Medical Centre</p>
  </div>

  <div class="contact-panel">
    <svg width="781" height="207" viewBox="0 0 781 207" aria-hidden="true">
      <defs>
        <linearGradient id="panelBlue" x1="0" x2="1" y1="0" y2="0">
          <stop offset="0" stop-color="#0f6fbf"/>
          <stop offset="1" stop-color="#22a4de"/>
        </linearGradient>
      </defs>
      <rect width="781" height="207" fill="url(#panelBlue)"/>
      <path d="M0,0 H781 V8 A44,44 0 0 0 737,52 H44 A44,44 0 0 0 0,8 Z" fill="#9fcb3d"/>
    </svg>
    <p class="tagline">where your care comes first</p>
    <address class="address">
      Kindle Grove Medical Centre<br>
      512 Tolvar Rd Dunmarra Court<br>
      Shopping Centre Corrin Vale<br>
      SA 5921
    </address>
    <ul class="links">
      <li>
        <span class="links__icon">
          <svg width="14" height="14" viewBox="0 0 24 24" aria-hidden="true"><path fill="#fff" d="M5 2h4l2 5-2.5 1.5a11 11 0 0 0 7 7L17 13l5 2v4a2 2 0 0 1-2 2A18 18 0 0 1 3 4a2 2 0 0 1 2-2z"/></svg>
        </span>
        08 8194 3627
      </li>
      <li>
        <span class="links__icon">
          <svg width="14" height="14" viewBox="0 0 24 24" aria-hidden="true" fill="none" stroke="#fff" stroke-width="2"><circle cx="12" cy="12" r="9"/><path d="M3 12h18M12 3c3 3 3 15 0 18M12 3c-3 3-3 15 0 18"/></svg>
        </span>
        kindlegrovemedicalcentre-example.com.au
      </li>
    </ul>
  </div>
</section>

<section class="card card--back" aria-label="Business card back">
  <h2 class="appointment__title">Your next appointment</h2>
  <div class="appointment__fields">
    <div class="field"><span class="field__label">Dr</span><span class="field__line"></span></div>
    <div class="field"><span class="field__label">Date</span><span class="field__line"></span></div>
    <div class="field"><span class="field__label">Time</span><span class="field__line"></span></div>
  </div>

  <svg class="booking-bubble" width="250" height="200" viewBox="0 0 250 200" aria-hidden="true">
    <defs>
      <linearGradient id="bubbleBlue" x1="0" x2="1" y1="1" y2="0">
        <stop offset="0" stop-color="#0f6fbf"/>
        <stop offset="1" stop-color="#2a9ee0"/>
      </linearGradient>
    </defs>
    <path d="M108,0 L104,55 L126,52 Z" fill="url(#bubbleBlue)"/>
    <ellipse cx="128" cy="124" rx="116" ry="73" fill="url(#bubbleBlue)"/>
  </svg>
  <p class="booking-bubble__text">
    <span class="booking-bubble__lead">Book online</span>
    <span class="booking-bubble__sub">easily and conveniently</span>
  </p>

  <div class="brand brand--faint">
    <p class="brand__name">Kindle Grove Medical Centre</p>
  </div>

  <p class="notice-strip">as soon as possible if unable to attend Cancellation fees apply if less than 2 hours notice</p>
</section>

</body>
</html>
```